bluecastle aquatics of northeast florida business card

I need a new attractive business card. I am planning on printing on very thick rounded corner stock and having painted edges. We are a swimming pool remodel, repair, and service company in north florida. Our current logo is red, white, and blue. It doesn't necessarily have to stay that way, I am open to other ideas. It will need to contain my name, work and cell numbers, email, website, and my contractor license number.

Target Market(s)

High end residential and commercial clients

Industry/Entity Type

Business

Contact Information for Business Card

Company name, employee name and title, work and cell phone numbers, email and website, and Contractor number.

our work scope should be on card somewhere: remodel ~ repair ~ service

logo or slight variation of logo also. (not necessarily set on keeping exact logo)

Colors

Designer to choose colors to be used in the design.

Requirements
Nice to have
• We deal with water so I think some sort of water element or just a color similar to pool water would be nice to integrate into design.

```html
<!DOCTYPE html>
<html lang="en">
<head>
<meta charset="utf-8">
<title>BlueCastle Aquatics – Business Card</title>
<link rel="stylesheet" href="https://fonts.googleapis.com/css2?family=Mulish:wght@400;500;600&display=swap">
<style>
  :root {
    --page: #f4fbfd;
    --pool-light: #b9e3ef;
    --pool-mid: #8fd0e3;
    --pool-deep: #6cb8cf;
    --brand-blue: #1c6fae;
    --accent-red: #e8383f;
    --accent-red-dark: #9e2d2f;
    --banner: #f8f7f4;
    --card: #ffffff;
    --card-edge: #eef1f3;
    --rule: #2a7ab8;
  }
  * { box-sizing: border-box; margin: 0; padding: 0; }
  html, body { width: 1200px; height: 1000px; overflow: hidden; }
  body {
    position: relative;
    background: var(--page);
    font-family: "Mulish", "Avenir Next", sans-serif;
  }

  .card {
    position: absolute;
    left: 307px;
    width: 588px;
    height: 360px;
    border-radius: 12px;
    overflow: hidden;
    box-shadow: 14px 10px 14px rgba(40, 70, 90, 0.18);
  }

  /* Front side */
  .card--front { top: 99px; }
  .card__water {
    position: absolute; inset: 0;
    background:
      radial-gradient(ellipse at 70% 30%, rgba(255,255,255,0.35), transparent 55%),
      linear-gradient(160deg, var(--pool-light) 0%, var(--pool-mid) 55%, var(--pool-deep) 100%);
  }
  .brand-banner {
    position: absolute;
    left: 0; top: 107px;
    width: 454px; height: 140px;
    background: linear-gradient(180deg, #ffffff 0%, var(--banner) 100%);
    box-shadow: 0 6px 0 rgba(40, 50, 55, 0.75), 0 22px 26px rgba(30, 60, 75, 0.35);
    display: flex; align-items: center;
    padding-left: 61px;
    gap: 9px;
  }
  .brand-banner__edge {
    position: absolute; right: 0; top: 0;
    width: 31px; height: 100%;
    background: linear-gradient(90deg, var(--accent-red-dark) 0 13px, #fbf9f6 13px 100%);
  }
  .brand-mark {
    width: 54px; height: 54px; border-radius: 50%;
    background: var(--accent-red);
    flex: none;
  }
  .brand-name {
    color: var(--brand-blue);
    font-weight: 600;
    text-transform: uppercase;
    line-height: 1.15;
  }
  .brand-name__main { display: block; font-size: 19px; letter-spacing: 1.6px; }
  .brand-name__sub {
    display: block; font-size: 11.5px; letter-spacing: 2.4px;
    border-bottom: 1px solid var(--brand-blue);
    padding-bottom: 1px; margin-top: 2px;
  }

  /* Back side */
  .card--back {
    top: 511px;
    background: var(--card);
    border: 2px solid var(--card-edge);
  }
  .contact { position: absolute; left: 26px; top: 32px; }
  .contact__name {
    color: var(--accent-red);
    font-size: 24px; font-weight: 400;
    letter-spacing: 0.3px;
  }
  .contact__title {
    color: #3a8cc4;
    font-size: 19px; font-weight: 400;
    margin-top: 3px;
  }
  .contact__rule {
    width: 424px; height: 1px;
    background: var(--rule);
    margin: 14px 0 13px;
  }
  .contact__list { list-style: none; color: var(--brand-blue); font-size: 18.5px; font-weight: 500; }
  .contact__list li { height: 33.5px; display: flex; }
  .contact__label { display: inline-block; width: 71px; }
  .contact__at { color: var(--accent-red); }

  .back-mark {
    position: absolute; right: 40px; top: 238px;
    width: 56px; height: 56px; border-radius: 50%;
    background: var(--accent-red);
  }
  .scope-wave {
    position: absolute; left: -2px; bottom: -2px;
    width: 588px; height: 62px;
  }
  .scope {
    position: absolute; left: 29px; bottom: 12px;
    color: #ffffff;
    font-size: 19.5px; font-weight: 500;
    letter-spacing: 0.2px;
  }
  .scope__sep { margin: 0 8px; }
</style>
</head>
<body>

  <section class="card card--front" aria-label="Business card front">
    <div class="card__water" role="img" aria-label="Rippling swimming pool water"></div>
    <div class="brand-banner">
      <span class="brand-mark"></span>
      <span class="brand-name">
        <span class="brand-name__main">BlueCastle Aquatics</span>
        <span class="brand-name__sub">Pool &amp; Spa Specialists</span>
      </span>
      <span class="brand-banner__edge"></span>
    </div>
  </section>

  <section class="card card--back" aria-label="Business card back">
    <div class="contact">
      <h1 class="contact__name">MARCUS DALE</h1>
      <p class="contact__title">Pool Technician</p>
      <div class="contact__rule"></div>
      <ul class="contact__list">
        <li><span class="contact__label">work :</span>904.555.0142</li>
        <li><span class="contact__label">cell&nbsp;&nbsp;&nbsp;:</span>904.555.0187</li>
        <li><span class="contact__label">email:</span>mdale<span class="contact__at">@</span>bluecastlepools.com</li>
        <li><span class="contact__label">web:</span>www.bluecastlepools-jax.com</li>
        <li>contractor #: 47</li>
      </ul>
    </div>
    <span class="back-mark"></span>
    <svg class="scope-wave" viewBox="0 0 588 62" preserveAspectRatio="none" aria-hidden="true">
      <defs>
        <linearGradient id="waveFill" x1="0" y1="0" x2="0" y2="1">
          <stop offset="0" stop-color="#a8dcea"/>
          <stop offset="1" stop-color="#7ec6db"/>
        </linearGradient>
      </defs>
      <path d="M0 22 C 80 8, 180 -2, 280 10 S 470 30, 588 0 L588 62 L0 62 Z" fill="url(#waveFill)"/>
    </svg>
    <p class="scope">REMODEL<span class="scope__sep">|</span>REPAIR<span class="scope__sep">|</span>SERVICE</p>
  </section>

</body>
</html>
```